Website for a Steadwell, an HVAC company.

We are a company that provides residential and commercial service. We don’t need any widgets other than a call to action where customers can message us. Though we have very few google reviews, they are all great and would like to see those populated. Simple and modern is the style. I included our logo and a pic of our vans.

Target Market(s)

Residential customers

Coding

Coded - Design and coding required

Number of Pages Required

1 page

Font styles to use
Sans Serif

Colors
0054AA
0677BA
7BADD7
CADEEF
E8F1F8
EE7325
F08F49
F5BC92
FAE3D3
FDF4ED

```html
<!DOCTYPE html>
<html lang="en">
<head>
<meta charset="utf-8">
<title>Steadwell Heating and Air</title>
<link href="https://fonts.googleapis.com/css2?family=Jost:wght@300;400;500;600;700;800&display=swap" rel="stylesheet">
<style>
:root{
  --blue-dark:#0054AA;--blue:#0677BA;--blue-mid:#7BADD7;--blue-soft:#CADEEF;--blue-pale:#E8F1F8;
  --orange:#EE7325;--orange-mid:#F08F49;--orange-soft:#F5BC92;--orange-pale:#FAE3D3;--orange-faint:#FDF4ED;
  --ink:#222831;--text:#4a4f57;--muted:#7b8089;--band:#efefef;--line:#e3e3e3;--footer:#0e1420;
}
*{box-sizing:border-box;margin:0;padding:0}
html,body{width:1200px;height:4228px;overflow:hidden}
body{font-family:'Jost',sans-serif;color:var(--ink);background:#fff;position:relative}
section,header,footer{position:relative;width:1200px;overflow:hidden}
.abs{position:absolute}
.btn{position:absolute;display:flex;align-items:center;justify-content:center;gap:8px;font-size:14px;font-weight:500;color:#fff;border-radius:3px}
.btn-blue{background:var(--blue)}
.btn-orange{background:var(--orange)}
.tag{position:absolute;background:var(--orange-pale);color:var(--orange);font-size:16px;padding:3px 8px;border-radius:2px}
.img{position:absolute}
/* header */
.site-header{height:63px;background:#fff}
.brand{position:absolute;display:flex;align-items:center;gap:6px}
.brand .dot{width:18px;height:18px;border-radius:50%;background:var(--orange)}
.brand span{font-weight:700;color:var(--blue-dark);letter-spacing:1px}
.nav a{position:absolute;top:23px;font-size:14px;color:var(--ink);text-decoration:none}
.nav a.active{color:var(--orange)}
.nav a.active::after{content:"";position:absolute;left:-14px;right:-14px;top:25px;height:2px;background:var(--orange)}
.call{position:absolute;left:934px;top:10px;width:99px;height:42px;background:var(--orange);border-radius:4px;color:#fff;text-align:center;font-size:9px;line-height:1.3;padding-top:7px}
.call b{display:block;font-size:12px;font-weight:600}
/* hero */
.hero{height:471px}
.hero .img{inset:0;background:linear-gradient(100deg,#3b4540 0%,#5a6761 35%,#7c8783 55%,#55615a 75%,#39433d 100%)}
.hero h1{position:absolute;left:166px;top:148px;font-size:33px;font-weight:800;color:#fff;letter-spacing:.5px}
.hero .sub{position:absolute;left:166px;top:193px;font-size:16px;font-weight:500;color:#fff}
.hero .lead{position:absolute;left:166px;top:240px;font-size:38px;font-weight:300;line-height:41px;color:#fff}
/* why */
.why{height:479px}
.center{position:absolute;left:0;width:1200px;text-align:center}
.why h2{top:113px;font-size:18px;font-weight:400;line-height:22px;color:var(--ink)}
.card{position:absolute;top:193px;width:205px;height:204px;background:#fff;box-shadow:0 2px 10px rgba(0,0,0,.07);border-radius:4px;padding:18px 17px}
.card .ic{width:36px;height:36px;border-radius:50%;background:var(--orange-pale);display:flex;align-items:center;justify-content:center}
.card h3{margin-top:30px;font-size:14px;font-weight:500;color:var(--orange)}
.card p{margin-top:10px;font-size:12px;line-height:16px;color:var(--text)}
/* about */
.about{height:607px;background:var(--band)}
.about h2{position:absolute;left:166px;top:84px;font-size:24px;font-weight:600;line-height:29px}
.about .copy{position:absolute;left:607px;top:44px;width:420px;font-size:12px;line-height:22px;color:var(--text)}
.svc h3{position:absolute;left:768px;top:398px;font-size:16px;font-weight:600;line-height:20px}
.svc p{position:absolute;left:768px;top:442px;width:266px;font-size:12px;line-height:16px;color:var(--text)}
/* brands */
.brands{height:289px}
.brands h2{top:74px;font-size:18px;font-weight:600}
.badge{position:absolute;top:132px;width:156px;height:72px;background:#fff;box-shadow:0 2px 8px rgba(0,0,0,.08);border-radius:4px;display:flex;align-items:center;justify-content:center}
.badge i{display:block;width:80px;height:26px;border-radius:4px;background:#cfd2d6}
/* style */
.style{height:498px;background:var(--band)}
.style h2{position:absolute;left:166px;top:55px;font-size:25px;font-weight:500}
.style .intro{position:absolute;left:166px;top:99px;width:450px;font-size:9px;line-height:15px;color:var(--text)}
.style .offer{position:absolute;right:167px;top:108px;font-size:11px;color:var(--muted)}
.work .img{top:161px;width:200px;height:243px}
.work .arrow{position:absolute;top:176px;width:20px;height:20px;border:1.5px solid var(--orange-mid);border-radius:50%}
.work h3{position:absolute;top:424px;font-size:14px;font-weight:600}
/* review */
.review{height:389px}
.review h2{position:absolute;left:174px;top:112px;font-size:37px;font-weight:500;line-height:38px}
.arw{position:absolute;top:221px;width:38px;height:38px;background:var(--blue-pale);display:flex;align-items:center;justify-content:center}
.quote-card{position:absolute;left:543px;top:65px;width:494px;height:273px;border:9px solid var(--orange-faint);outline:1px solid var(--orange-pale);border-radius:12px;background:#fff}
.stars{position:absolute;left:30px;top:30px;display:flex;gap:6px}
.who{position:absolute;left:30px;top:82px;display:flex;gap:10px}
.who .av{width:26px;height:26px;border-radius:50%;background:var(--orange-soft);flex:none}
.who b{font-size:10px;font-weight:600}
.who p{font-size:10px;line-height:14px;color:var(--text);width:400px;margin-top:4px}
.qmark{position:absolute;right:28px;bottom:10px;font-size:90px;line-height:1;color:var(--orange-pale);font-weight:300}
/* blog */
.blog{height:574px;background:var(--blue-pale)}
.blog h2{top:81px;font-size:18px;font-weight:500}
.post{position:absolute;top:110px;width:278px;height:431px;background:#fff;border-radius:3px;padding:23px 21px}
.post .img{position:relative;width:236px;height:202px}
.meta{margin-top:25px;display:flex;gap:14px;font-size:9px;color:var(--muted);align-items:center}
.meta span{display:flex;gap:5px;align-items:center}
.post h3{margin-top:10px;font-size:13px;font-weight:400;line-height:18px}
.post p{margin-top:10px;font-size:8px;line-height:12px;color:var(--muted)}
.more{margin-top:18px;width:106px;height:35px;border:1px solid var(--blue);border-radius:3px;color:var(--blue);font-size:10px;font-weight:500;display:flex;align-items:center;justify-content:center;gap:7px}
/* contact */
.contact{height:537px}
.contact>.img{inset:0;background:linear-gradient(120deg,#4a4136,#6b5b48 40%,#3b3c45 70%,#2c2f37)}
.panel{position:absolute;left:166px;top:67px;width:867px;height:401px;background:rgba(255,255,255,.9);border-radius:12px}
.panel h3{position:absolute;font-size:16px;font-weight:400;line-height:21px}
.panel .hint{position:absolute;left:38px;top:100px;width:260px;font-size:10px;line-height:13px;color:var(--text)}
.reach{position:absolute;left:38px;display:flex;gap:14px;align-items:center}
.reach .ic{width:36px;height:36px;background:var(--orange-faint);border-radius:4px;display:flex;align-items:center;justify-content:center}
.reach small{display:block;font-size:8px;color:var(--muted)}
.reach b{font-size:10px;font-weight:400;color:var(--text)}
.social{position:absolute;left:38px;top:265px;width:277px;height:98px;background:var(--orange-faint);border-radius:6px;padding:20px 22px}
.social p{font-size:10px}
.social .row{margin-top:22px;display:flex;gap:10px;align-items:center}
.social .row i{width:26px;height:26px;border-radius:50%;background:#fff;display:block}
.social .row i.on{background:var(--orange)}
.field{position:absolute;background:#fff;border:1px solid var(--line);border-radius:2px;font-size:9px;color:var(--muted);padding:10px 11px}
/* footer */
.site-footer{height:321px;background:var(--footer);color:#fff}
.site-footer .bg{position:absolute;inset:0;background:linear-gradient(90deg,#121a2a,#0b0f18 50%,#141c2c)}
.site-footer .about-f{position:absolute;left:166px;top:140px;width:260px;font-size:11px;line-height:14px}
.fcol{position:absolute;top:53px;font-size:12px;line-height:22.5px}
.fcol h4{font-size:12px;font-weight:600;margin-bottom:3px}
.site-footer .rule{position:absolute;left:166px;right:167px;top:233px;height:1px;background:rgba(255,255,255,.35)}
.site-footer .legal{position:absolute;top:264px;font-size:12px}
</style>
</head>
<body>

<header class="site-header">
  <div class="brand" style="left:166px;top:20px"><i class="dot"></i><span style="font-size:13px">STEADWELL</span></div>
  <nav class="nav">
    <a class="active" style="left:588px">Home</a>
    <a style="left:656px">About</a>
    <a style="left:716px">Services</a>
    <a style="left:794px">Blog</a>
    <a style="left:851px">Contact</a>
  </nav>
  <a class="call">Call Now<b>555 010 4477</b></a>
</header>

<section class="hero">
  <div class="img" role="img" aria-label="Steadwell branded service pickup truck parked in front of trees under an overcast sky"></div>
  <h1>TRUSTED FOR COMFORT</h1>
  <p class="sub">Steadwell Cooling &amp; Heating</p>
  <p class="lead">Reliable Residential &amp;<br>Commercial HVAC<br>Services</p>
  <a class="btn btn-blue" style="left:166px;top:381px;width:165px;height:33px">Get Free Estimation</a>
  <a class="btn btn-orange" style="left:338px;top:381px;width:181px;height:33px">Book an Appointment</a>
</section>

<section class="why">
  <div class="center" style="top:72px"><span class="tag" style="position:static">Why Choose Us</span></div>
  <h2 class="center">Steadwell Heating and Air your trusted<br>partner in home comfort.</h2>
  <div class="card" style="left:166px"><div class="ic"><svg width="16" height="16" viewBox="0 0 16 16"><circle cx="8" cy="6" r="4" fill="var(--orange)"/><path d="M5 9l-1 6 4-2 4 2-1-6" fill="var(--orange)"/></svg></div><h3>Quality Service</h3><p>Our experienced technicians are committed to delivering quality service and ensuring your HVAC system operates at its best.</p></div>
  <div class="card" style="left:387px"><div class="ic"><svg width="16" height="16" viewBox="0 0 16 16"><circle cx="9" cy="5" r="3.5" fill="var(--orange)"/><path d="M1 12h4l3 2 6-3" stroke="var(--orange)" stroke-width="2" fill="none"/></svg></div><h3>Affordability</h3><p>We offer competitive pricing and transparent quotes to get your needed services without breaking the bank.</p></div>
  <div class="card" style="left:607px"><div class="ic"><svg width="16" height="16" viewBox="0 0 16 16"><circle cx="8" cy="10" r="4" fill="var(--orange)"/><circle cx="3" cy="5" r="1.6" fill="var(--orange)"/><circle cx="8" cy="3" r="1.6" fill="var(--orange)"/><circle cx="13" cy="5" r="1.6" fill="var(--orange)"/></svg></div><h3>Customer Satisfaction</h3><p>Your satisfaction is our priority. We work diligently to exceed your expectations and provide personalized solutions.</p></div>
  <div class="card" style="left:829px"><div class="ic"><svg width="16" height="16" viewBox="0 0 16 16"><circle cx="8" cy="8" r="6" fill="none" stroke="var(--orange)" stroke-width="2"/><circle cx="8" cy="7" r="2" fill="var(--orange)"/></svg></div><h3>Community Focus</h3><p>We’re proud to serve Charleston and its surrounding islands. It is our way giving back to the community .</p></div>
</section>

<section class="about">
  <span class="tag" style="left:166px;top:46px">About</span>
  <h2>Heating and Air Conditioning<br>Services You Can Depend On</h2>
  <p class="copy">Since 2003, Steadwell Heating and Air has been the go-to provider for reliable and affordable heating and cooling solutions in Charleston, SC, and surrounding areas. With over 20 years of experience, we have built a reputation for excellence, ensuring homes and businesses stay comfortable year-round.</p>
  <a class="btn btn-blue" style="left:607px;top:166px;width:111px;height:32px">Learn more</a>
  <div class="img" role="img" aria-label="Technician in blue overalls reviewing a clipboard with a customer in a workshop" style="left:166px;top:233px;width:584px;height:333px;background:linear-gradient(120deg,#c9ccc9,#8e9aa1 45%,#6a7a88 70%,#aeb3ad)"></div>
  <svg class="abs" style="left:427px;top:368px" width="62" height="62" viewBox="0 0 62 62"><circle cx="31" cy="31" r="28" fill="rgba(255,255,255,.25)" stroke="#fff" stroke-width="3"/><path d="M25 19l18 12-18 12z" fill="#fff"/></svg>
  <div class="svc">
    <div class="img" role="img" aria-label="Technician in uniform holding a clipboard at a doorway" style="left:768px;top:233px;width:266px;height:153px;background:linear-gradient(90deg,#7f9fb8,#a9adab 40%,#b8b3a8)"></div>
    <h3>Residential Heating &amp; Cooling<br>Services</h3>
    <p>Reliable HVAC solutions for year-round comfort. Our expert technicians quickly diagnose and fix issues while ensuring long-term system efficiency.</p>
    <a class="btn btn-blue" style="left:768px;top:532px;width:104px;height:33px">Book Now</a>
  </div>
</section>

<section class="brands">
  <h2 class="center">Major HVAC Equipment Brands We’re Partnered With</h2>
  <div class="badge" style="left:168px"><i></i></div>
  <div class="badge" style="left:344px"><i style="width:70px;height:40px"></i></div>
  <div class="badge" style="left:520px"><i style="background:#f3c2b0"></i></div>
  <div class="badge" style="left:694px"><i style="width:76px;height:30px"></i></div>
  <div class="badge" style="left:872px"><i style="width:44px;height:44px;border-radius:50%"></i></div>
</section>

<section class="style">
  <h2>Style and Finishing</h2>
  <p class="intro">Transform your living spaces with our range of stylish accessories, including decorative vases, sculptures, and wall art. Each piece is carefully chosen to add visual interest and personality to your home, creating a welcoming and inviting atmosphere for you and your guests to enjoy.</p>
  <a class="btn btn-blue" style="left:899px;top:67px;width:124px;height:33px">Book Service</a>
  <p class="offer">get 50% offer til 30 nov 2025</p>
  <div class="work">
    <div class="img" role="img" aria-label="Technician in a hard hat repairing an outdoor heating unit" style="left:166px;background:linear-gradient(160deg,#d8d8d8,#b9b7a7 50%,#6f7e94)"></div><i class="arrow" style="left:332px"></i><h3 style="left:166px">Heating Repair</h3>
    <div class="img" role="img" aria-label="Technician servicing a wall-mounted air conditioner" style="left:389px;background:linear-gradient(160deg,#e6e6e6,#c3c8cf 50%,#5d7390)"></div><i class="arrow" style="left:555px"></i><h3 style="left:389px">AC Repair</h3>
    <div class="img" role="img" aria-label="Technician kneeling to check refrigerant gauges on a heating unit" style="left:611px;background:linear-gradient(160deg,#ececec,#c9c4a9 50%,#41598a)"></div><h3 style="left:611px">Heating Maintenance</h3>
    <div class="img" role="img" aria-label="Technician cleaning an indoor air conditioning unit" style="left:833px;background:linear-gradient(160deg,#dcdcdc,#c8c8c8 50%,#6d6f74)"></div><i class="arrow" style="left:999px"></i><h3 style="left:833px">AC Maintenance</h3>
  </div>
</section>

<section class="review">
  <span class="tag" style="left:174px;top:80px">Client Review</span>
  <h2>Our partners. Our<br>Friends. They love us.</h2>
  <span class="arw" style="left:174px"><svg width="16" height="12" viewBox="0 0 16 12"><path d="M15 6H2M6 1L1 6l5 5" stroke="var(--blue)" stroke-width="1.5" fill="none"/></svg></span>
  <span class="arw" style="left:224px"><svg width="16" height="12" viewBox="0 0 16 12"><path d="M1 6h13M10 1l5 5-5 5" stroke="var(--blue)" stroke-width="1.5" fill="none"/></svg></span>
  <div class="quote-card">
    <div class="stars">
      <svg width="22" height="22" viewBox="0 0 24 24"><path d="M12 2l3 7 7 .6-5.4 4.7 1.7 7.2L12 17.8 5.7 21.5l1.7-7.2L2 9.6 9 9z" fill="var(--orange)"/></svg>
      <svg width="22" height="22" viewBox="0 0 24 24"><path d="M12 2l3 7 7 .6-5.4 4.7 1.7 7.2L12 17.8 5.7 21.5l1.7-7.2L2 9.6 9 9z" fill="var(--orange)"/></svg>
      <svg width="22" height="22" viewBox="0 0 24 24"><path d="M12 2l3 7 7 .6-5.4 4.7 1.7 7.2L12 17.8 5.7 21.5l1.7-7.2L2 9.6 9 9z" fill="var(--orange)"/></svg>
      <svg width="22" height="22" viewBox="0 0 24 24"><path d="M12 2l3 7 7 .6-5.4 4.7 1.7 7.2L12 17.8 5.7 21.5l1.7-7.2L2 9.6 9 9z" fill="var(--orange)"/></svg>
      <svg width="22" height="22" viewBox="0 0 24 24"><path d="M12 2l3 7 7 .6-5.4 4.7 1.7 7.2L12 17.8 5.7 21.5l1.7-7.2L2 9.6 9 9z" fill="var(--orange)"/></svg>
    </div>
    <div class="who"><i class="av" role="img" aria-label="Reviewer avatar"></i><div><b>Marla Jensen</b><p>“Lorem ipsum dolor sit amet, consectetur adipiscing elit, sed do eiusmod tempor incididunt ut labore et dolore magna aliqua. Ut enim ad minim veniam, quis nostrud exercitation ullamco laboris nisi ut aliquip ex ea commodo consequat.”</p></div></div>
    <span class="qmark">99</span>
  </div>
</section>

<section class="blog">
  <div class="center" style="top:44px"><span class="tag" style="position:static">Blog</span></div>
  <h2 class="center">Expert Tips &amp; Insights for a Comfortable Home</h2>
  <article class="post" style="left:166px">
    <div class="img" role="img" aria-label="Technician connecting gauges to an outdoor unit" style="background:linear-gradient(150deg,#c9c7c2,#7f8791 55%,#3f5d8c)"></div>
    <div class="meta"><span>▢ 17 Oct, 2020</span><span>▤ 5 min read</span></div>
    <h3>Duis magna risus, convallis vel purus eu, sollicidin volutpat velit.</h3>
    <p>Praesent turpis quam, dapibus id diam a, cursus lobortis mi. Praesent nec lorem eget nisi sodales vehicula etiam sagittis dapibus.</p>
    <div class="more">Read More <span>→</span></div>
  </article>
  <article class="post" style="left:461px">
    <div class="img" role="img" aria-label="Technician working on an outdoor air conditioning condenser" style="background:linear-gradient(150deg,#b9b9b9,#8b8f95 55%,#5b5f66)"></div>
    <div class="meta"><span>▢ 24 May, 2020</span><span>▤ 5 min read</span></div>
    <h3>Duis magna risus, convallis vel purus eu, sollicidin volutpat velit.</h3>
    <p>Praesent turpis quam, dapibus id diam a, cursus lobortis mi. Praesent nec lorem eget nisi sodales vehicula etiam sagittis dapibus.</p>
    <div class="more">Read More <span>→</span></div>
  </article>
  <article class="post" style="left:755px">
    <div class="img" role="img" aria-label="Technician kneeling beside an outdoor HVAC cabinet" style="background:linear-gradient(150deg,#8fa37a,#5c6a78 55%,#2f4f8f)"></div>
    <div class="meta"><span>▢ 1 Feb, 2020</span><span>▤ 5 min read</span></div>
    <h3>Duis magna risus, convallis vel purus eu, sollicidin volutpat velit.</h3>
    <p>Praesent turpis quam, dapibus id diam a, cursus lobortis mi. Praesent nec lorem eget nisi sodales vehicula etiam sagittis dapibus.</p>
    <div class="more">Read More <span>→</span></div>
  </article>
</section>

<section class="contact">
  <div class="img" role="img" aria-label="Steadwell service van parked beside a brick building"></div>
  <div class="panel">
    <h3 style="left:38px;top:40px">Have a question or need HVAC<br>services?</h3>
    <p class="hint">We’re here to help! Send us a message, and our team will get back to you within 48 hours. Let’s keep your home comfortable!</p>
    <div class="reach" style="top:158px"><span class="ic"><svg width="14" height="14" viewBox="0 0 24 24"><path d="M6 2l4 4-2 3c1 3 4 6 7 7l3-2 4 4-3 4C10 21 3 14 2 5z" fill="none" stroke="var(--orange)" stroke-width="2"/></svg></span><div><small>Call me now</small><b>555 010 4477</b></div></div>
    <div class="reach" style="top:201px"><span class="ic"><svg width="14" height="12" viewBox="0 0 14 12"><rect x="1" y="1" width="12" height="10" fill="none" stroke="var(--orange)" stroke-width="1.4"/><path d="M1 1l6 5 6-5" fill="none" stroke="var(--orange)" stroke-width="1.4"/></svg></span><div><small>Chat with me</small><b>hello@steadwellhvac.com</b></div></div>
    <div class="social"><p>Follow me on social media</p><div class="row"><span style="width:14px;height:1px;background:var(--ink)"></span><i></i><i></i><i class="on"></i><i></i></div></div>
    <h3 style="left:394px;top:50px">Contact Us</h3>
    <div class="field" style="left:394px;top:86px;width:212px;height:31px">Full Name</div>
    <div class="field" style="left:617px;top:86px;width:212px;height:31px">Email Adress</div>
    <div class="field" style="left:394px;top:129px;width:435px;height:29px">Subject</div>
    <div class="field" style="left:394px;top:171px;width:212px;height:28px">Services <span style="float:right">⌄</span></div>
    <div class="field" style="left:617px;top:171px;width:212px;height:28px">Budgets <span style="float:right">⌄</span></div>
    <div class="field" style="left:394px;top:211px;width:435px;height:79px">Message</div>
    <a class="btn btn-orange" style="left:394px;top:314px;width:148px;height:46px;font-size:11px;border-radius:4px">Send Message →</a>
  </div>
</section>

<footer class="site-footer">
  <div class="bg" role="img" aria-label="Faint Steadwell service truck behind dark overlay"></div>
  <div class="brand" style="left:166px;top:98px"><i class="dot"></i><span style="font-size:14px;color:var(--blue-mid)">STEADWELL</span></div>
  <p class="about-f">Steadwell Heating and Air is more than just an HVAC company; we’re your partners in creating a comfortable living environment.</p>
  <div class="fcol" style="left:524px"><h4>Important Links</h4>Home<br>About<br>Services<br>Blog<br>Contact</div>
  <div class="fcol" style="left:693px"><h4>Other Links</h4>Area We Serve<br>Heating<br>Cooling<br>Energy Saving<br>Products</div>
  <div class="fcol" style="left:845px"><h4>Open Hours</h4>Mon - Fri&nbsp; 7:00 AM To 6:00 PM<br>Saturday&nbsp; 8:00 AM To 3:00 PM<br>Sunday&nbsp; Appointment Only</div>
  <div class="rule"></div>
  <p class="legal" style="left:166px">Steadwell Heating and Air @ 2025. All rights reserved.</p>
  <p class="legal" style="left:756px">Terms</p>
  <p class="legal" style="left:821px">Privacy</p>
  <p class="legal" style="left:890px">Legal Policy</p>
  <p class="legal" style="left:990px;display:flex;gap:6px;align-items:center"><svg width="14" height="14" viewBox="0 0 16 16"><circle cx="8" cy="8" r="7" fill="none" stroke="#fff" stroke-width="1.3"/><path d="M1 8h14M8 1c3 3 3 11 0 14M8 1c-3 3-3 11 0 14" fill="none" stroke="#fff" stroke-width="1.1"/></svg>EN</p>
</footer>

</body>
</html>
```